Es wurden alle Wünsche immer rasch und professionell umgesetzt. Wir sind rundum zufrieden. Vielen Dank :)
Wir sind ein junges Fotografen-Paar, und wollen heuer neu durchstarten mit Kinder- und Neugeborenen Fotografie. Unsere Zielgruppe sind vor allem schwangere Frauen, die frühzeitig ein Newborn-Shooting oder vorab ein Schwangerschafts-Shooting buchen möchten. Wir sind auf der Suche nach einem minimalistischen Flyer zum Auslegen in diversen Einrichtungen, und einer dazu passenden Visitenkarte.
Wir haben kein Logo, möchten aber auch nichts aufwendiges. Es darf auch ein passendes fertiges Stock-Logo sein.
Wir lieben den BoHo Stil, und fotografieren auch fast ausschließlich in diesem. Dementsprechend stellen wir uns unseren Flyer bzw unsere Visitenkarte minimalistisch vor. Da es um Kinder und Babys geht, ziehen wir die Farbe Altrosa/Rosé vor, eventuell als Akzentfarbe, oder auch als Hintergrundfarbe.
Der Flyer zum Auslegen in Tagesstätten oder zB im Krankenhaus stellen wir uns quadratisch vor (einfacher Flyer/Doppelseitig).
Die Visitenkarte eventuell Hochformat, jedoch sind wir hier total offen. Meine Partnerin meint ein 'BOHO-Regenbogen' wäre bestimmt sehr lieb, jedoch soll dies keine Voraussetzung sein.
Auf der Vorderseite soll unser Logo und ein Foto sein (Baby/Newborn).
Auf der Rückseite mindestens 3-4 unserer Bilder, und einen kurzen Text plus Kontaktdaten.

```html
<!DOCTYPE html>
<html lang="de">
<head>
<meta charset="utf-8">
<title>kleinlicht – Flyer Rückseite</title>
<link href="https://fonts.googleapis.com/css2?family=Source+Sans+3:wght@400;600;700&display=swap" rel="stylesheet">
<style>
  :root {
    --paper: #ffffff;
    --mist: #d9d3d3;
    --mist-band: rgba(200, 194, 194, 0.55);
    --rose-veil: rgba(176, 124, 118, 0.62);
    --rose-pale: #ecd4cc;
    --mauve: #9b737a;
    --mauve-title: #a27776;
    --rose-text: #c7a29b;
    --ink: #40454e;
    --frame: #8d8080;
  }
  * { margin: 0; padding: 0; box-sizing: border-box; }
  html, body { width: 1200px; height: 1200px; overflow: hidden; background: var(--paper); }
  body { font-family: "Source Sans 3", "Helvetica Neue", Arial, sans-serif; }

  .flyer { position: relative; width: 1200px; height: 1200px; overflow: hidden; background: var(--paper); }

  .photo { position: absolute; }
  .photo--newborn {
    left: 0; top: 0; width: 606px; height: 410px;
    background: radial-gradient(ellipse at 45% 45%, #b08a86 0%, #6e4f52 45%, #3a2a2c 100%);
  }
  .photo--rocking-horse {
    left: 725px; top: 0; width: 475px; height: 657px;
    background: linear-gradient(160deg, #3b2a22 0%, #5a3f30 35%, #c98b86 60%, #4a3226 100%);
  }
  .photo--path-walk {
    left: 725px; top: 657px; width: 475px; height: 543px;
    background: linear-gradient(180deg, #7c8a62 0%, #9e9a86 40%, #b9ab93 70%, #7f7256 100%);
  }

  .mist-column { position: absolute; left: 606px; top: 0; width: 111px; height: 410px; background: var(--mist); }
  .mist-band { position: absolute; left: 0; top: 410px; width: 725px; height: 86px; background: var(--mist-band); }

  .decor { position: absolute; left: 0; top: 0; width: 1200px; height: 1200px; }

  .intro { position: absolute; left: 54px; top: 536px; width: 410px; text-align: center; }
  .intro__title { font-size: 31px; font-weight: 700; color: var(--mauve-title); line-height: 1.2; }
  .intro__text { margin-top: 4px; font-size: 21px; line-height: 24.5px; color: var(--rose-text); hyphens: manual; }

  .veil { position: absolute; left: 520px; top: 290px; width: 368px; height: 705px; background: var(--rose-veil); }
  .veil__copy { position: absolute; left: 29px; width: 310px; text-align: center; color: #fff; font-size: 20.5px; line-height: 28.5px; hyphens: manual; }
  .veil__copy--first { top: 68px; }
  .veil__copy--second { top: 342px; }
  .veil__rule { position: absolute; left: 24px; top: 309px; width: 318px; height: 1px; background: rgba(255,255,255,0.75); }

  .brand { position: absolute; left: 62px; top: 1102px; display: flex; align-items: center; gap: 14px; }
  .brand__dot { width: 58px; height: 58px; border-radius: 50%; background: var(--rose-pale); }
  .brand__name { font-size: 34px; font-weight: 400; color: var(--mauve); letter-spacing: 0.5px; }

  .divider { position: absolute; left: 409px; top: 1058px; width: 2px; height: 112px; background: var(--mauve); }

  .contact { position: absolute; left: 432px; top: 1057px; list-style: none; }
  .contact__item { display: flex; align-items: center; gap: 14px; height: 40px; font-size: 16px; font-weight: 700; color: var(--ink); }
  .contact__icon { width: 30px; height: 30px; }
</style>
</head>
<body>
<main class="flyer">
  <div class="photo photo--newborn" role="img" aria-label="Foto: schlafendes Neugeborenes mit Häkelhaarband auf Strickdecke"></div>
  <div class="mist-column"></div>
  <div class="photo photo--rocking-horse" role="img" aria-label="Foto: lachendes Kleinkind im rosa Kleid auf einem Schaukelpferd vor Holzwand mit Lichterkette"></div>
  <div class="photo photo--path-walk" role="img" aria-label="Foto: Kleinkind mit Mütze und Koffer läuft einen Feldweg entlang"></div>
  <div class="mist-band"></div>

  <svg class="decor" viewBox="0 0 703 703" aria-hidden="true">
    <defs>
      <clipPath id="left-field"><rect x="-20" y="0" width="324" height="703"/></clipPath>
    </defs>
    <g clip-path="url(#left-field)">
      <path class="rainbow rainbow--pale" d="M-10,468 C140,468 282,430 282,352" fill="none" stroke="#ecd4cc" stroke-width="46" stroke-linecap="round"/>
      <path class="rainbow rainbow--mauve" d="M-10,530 C170,530 300,490 345,418" fill="none" stroke="#9b737a" stroke-width="46"/>
      <g class="dot-arc" fill="#40454e">
        <circle cx="4" cy="625" r="8"/>
        <circle cx="45" cy="617" r="8"/>
        <circle cx="86" cy="614" r="8"/>
        <circle cx="128" cy="607" r="8"/>
        <circle cx="172" cy="593" r="8"/>
        <circle cx="215" cy="577" r="8"/>
        <circle cx="256" cy="553" r="8"/>
        <circle cx="290" cy="528" r="8"/>
      </g>
    </g>
  </svg>

  <section class="intro">
    <h1 class="intro__title">Lorem ipsum</h1>
    <p class="intro__text">At vero eos et accusamus et iusto odio dignissimos ducimus qui blanditiis prae&shy;sentium voluptatum deleniti atque cor&shy;rupti quos dolores et quas molestias excepturi sint occaecati cupiditate non provident.</p>
  </section>

  <section class="veil">
    <p class="veil__copy veil__copy--first">Sed ut perspiciatis unde omnis iste natus error sit voluptatem accusantium doloremque lau&shy;dantium, totam rem aperiam, eaque ipsa quae ab illo inven&shy;tore veritatis et quasi architecto beatae vitae dicta sunt explica&shy;bo.</p>
    <div class="veil__rule"></div>
    <p class="veil__copy veil__copy--second">Nemo enim ipsam voluptatem quia voluptas sit aspernatur aut odit aut fugit, sed quia consequuntur magni dolores eos qui ratione voluptatem sequi nesciunt. Neque porro quisquam est, qui dolorem ipsum quia dolor sit amet, consectetur, adipisci velit, sed quia non numquam eius modi tempora incidunt ut labore.</p>
  </section>

  <div class="brand">
    <span class="brand__dot"></span>
    <span class="brand__name">kleinlicht</span>
  </div>

  <div class="divider"></div>

  <ul class="contact">
    <li class="contact__item">
      <svg class="contact__icon" viewBox="0 0 30 30" aria-hidden="true"><circle cx="15" cy="15" r="15" fill="#40454e"/><path d="M10.5 8.5c.8-.6 1.8-.4 2.2.4l1.2 2.3c.3.7.1 1.4-.5 1.8l-.8.6c.8 1.7 2 3 3.7 3.8l.6-.8c.4-.6 1.2-.8 1.8-.5l2.3 1.2c.8.4 1 1.4.4 2.2l-.8 1c-.7.8-1.8 1.1-2.8.8-4-1.3-7.2-4.5-8.4-8.5-.3-1 0-2.1.8-2.8z" fill="#fff"/></svg>
      <span>2468– 1357</span>
    </li>
    <li class="contact__item">
      <svg class="contact__icon" viewBox="0 0 30 30" aria-hidden="true"><circle cx="15" cy="15" r="15" fill="#40454e"/><rect x="8" y="10" width="14" height="10" rx="1" fill="#fff"/><path d="M8.5 10.5 15 15.5l6.5-5" fill="none" stroke="#40454e" stroke-width="1.4"/></svg>
      <span>info@kleinlicht-foto.de</span>
    </li>
    <li class="contact__item">
      <svg class="contact__icon" viewBox="0 0 30 30" aria-hidden="true"><circle cx="15" cy="15" r="15" fill="#40454e"/><g fill="none" stroke="#fff" stroke-width="1.5"><circle cx="15" cy="15" r="7"/><ellipse cx="15" cy="15" rx="3" ry="7"/><path d="M8 15h14M9.2 11.5h11.6M9.2 18.5h11.6"/></g></svg>
      <span>www.kleinlicht-foto.de/</span>
    </li>
  </ul>

  <svg class="decor decor--frame" viewBox="0 0 1200 1200" aria-hidden="true">
    <path d="M12 8 L1192 12 L1190 1192 L8 1190 Z" fill="none" stroke="#8d8080" stroke-width="1.6" stroke-linejoin="round"/>
  </svg>
</main>
</body>
</html>
```